10 years employment working at VALMOR

I need a certificate designed for employees to recognise 10 year tenure at our company. 1. You need to feature our logo 2. Our Grounds design. 3. Our Purpose: To provide support and service that enables disadvantaged and/or unemployed people in our community to secure and sustain meaningful employment. 4. A space for the employees name 5. A space for our Lena Brookfield CEO and Marcus Elwyn, Chair of Board to sign 6. VALMOR Values your Service and Contribution

Target Market(s)

Employees

Industry/Entity Type

Employment Agency

Font styles to use
Sans Serif

Requirements
Must have
• Every thing from number 1 to 6 above in the description

```html
<!DOCTYPE html>
<html lang="en">
<head>
<meta charset="utf-8">
<title>VALMOR 10 Years Tenure Certificate</title>
<link rel="stylesheet" href="https://fonts.googleapis.com/css2?family=Lato:wght@700;900&family=Cinzel:wght@400;700&family=Oswald:wght@500;600&display=swap">
<style>
  :root {
    --ground-dark: #0f2f33;
    --ground-teal: #13655a;
    --ground-green: #2fa25a;
    --ground-orange: #d08a3a;
    --panel: #f6f6f6;
    --panel-edge: #ececec;
    --ink: #333333;
    --ink-soft: #3a3a3a;
    --ribbon: #050505;
    --gold-light: #f7d46a;
    --gold: #d9a21c;
    --gold-deep: #9a6a0a;
    --rule: #d6d4c8;
  }
  * { margin: 0; padding: 0; box-sizing: border-box; }
  html, body { width: 1200px; height: 902px; overflow: hidden; background: #ffffff; }

  .certificate {
    position: relative;
    width: 1200px;
    height: 902px;
    overflow: hidden;
  }

  .grounds-pattern {
    position: absolute;
    inset: 0;
    background:
      radial-gradient(circle at 15% 20%, var(--ground-green) 0, transparent 28%),
      radial-gradient(circle at 85% 85%, var(--ground-orange) 0, transparent 18%),
      radial-gradient(circle at 92% 30%, var(--ground-teal) 0, transparent 35%),
      radial-gradient(circle at 10% 80%, var(--ground-teal) 0, transparent 35%),
      linear-gradient(135deg, var(--ground-teal), var(--ground-dark) 60%, var(--ground-teal));
  }

  .panel {
    position: absolute;
    left: 61px;
    top: 74px;
    width: 1074px;
    height: 762px;
    background: linear-gradient(90deg, #ffffff, var(--panel) 70%, var(--panel-edge));
    border-top-right-radius: 115px;
    border-bottom-left-radius: 190px;
    box-shadow: 0 6px 14px rgba(0,0,0,0.35);
  }

  .ribbon {
    position: absolute;
    left: 104px;
    top: 74px;
    width: 285px;
    height: 250px;
    background: var(--ribbon);
  }

  .tenure-seal {
    position: absolute;
    left: 101px;
    top: 223px;
    width: 296px;
    height: 296px;
    border-radius: 50%;
    background: radial-gradient(circle at 40% 35%, var(--gold-light), var(--gold) 55%, var(--gold-deep));
    border: 14px solid var(--gold-deep);
    box-shadow: inset 0 0 0 4px var(--gold-light);
    display: flex;
    flex-direction: column;
    align-items: center;
    justify-content: center;
    font-family: "Oswald", sans-serif;
    color: #111;
    line-height: 1;
    text-align: center;
  }
  .tenure-seal .years { font-size: 52px; font-weight: 600; color: #ffffff; }
  .tenure-seal .tenure { font-size: 34px; font-weight: 500; margin-top: 6px; }
  .tenure-seal .company { font-size: 38px; font-weight: 600; margin-top: 6px; }

  .brand-name {
    position: absolute;
    left: 110px;
    top: 690px;
    width: 280px;
    text-align: center;
    font-family: "Lato", sans-serif;
    font-weight: 900;
    font-size: 62px;
    color: #111111;
    letter-spacing: 1px;
  }

  .title {
    position: absolute;
    left: 442px;
    top: 128px;
    font-family: "Lato", sans-serif;
    font-weight: 900;
    font-size: 94px;
    color: var(--ink);
    letter-spacing: 1px;
    line-height: 1;
  }

  .presentation {
    position: absolute;
    left: 450px;
    top: 256px;
    font-family: "Cinzel", serif;
    font-size: 23px;
    line-height: 26px;
    color: #222;
  }

  .name-line {
    position: absolute;
    left: 454px;
    top: 430px;
    width: 590px;
    height: 2px;
    background: var(--rule);
  }

  .message {
    position: absolute;
    left: 445px;
    top: 493px;
    width: 620px;
    font-family: "Cinzel", serif;
    color: var(--ink-soft);
  }
  .message h2 { font-size: 16px; font-weight: 700; margin-bottom: 12px; }
  .message p { font-size: 16px; line-height: 20px; }

  .signatory {
    position: absolute;
    top: 744px;
    width: 240px;
    font-family: "Cinzel", serif;
    font-size: 14px;
    color: #222;
  }
  .signatory::before {
    content: "";
    display: block;
    height: 1px;
    background: var(--rule);
    margin-bottom: 32px;
  }
  .signatory strong { font-weight: 700; }
  .signatory.ceo { left: 445px; }
  .signatory.chair { left: 779px; }
</style>
</head>
<body>
  <main class="certificate">
    <div class="grounds-pattern" role="img" aria-label="VALMOR Grounds design: green, teal and orange patterned artwork"></div>

    <section class="panel"></section>
    <div class="ribbon"></div>

    <div class="tenure-seal">
      <span class="years">10 YEARS</span>
      <span class="tenure">TENURE</span>
      <span class="company">VALMOR</span>
    </div>

    <div class="brand-name">valmor</div>

    <h1 class="title">CERTIFICATE</h1>
    <p class="presentation">This certificate is proudly presented<br>for honorable achievement to</p>

    <div class="name-line"></div>

    <div class="message">
      <h2>Lorem Ipsum is simply dummy text</h2>
      <p>Lorem Ipsum is simply dummy text of the printing and<br>typesetting industry. Lorem Ipsum has been the industry's<br>standard dummy text</p>
    </div>

    <div class="signatory ceo"><strong>LENA BROOKFIELD,</strong> CEO</div>
    <div class="signatory chair"><strong>MARCUS ELWYN,</strong> CHAIR OF BOARD</div>
  </main>
</body>
</html>
```